Yoga Training Cerificate

Design a certificate of graduation from a Vinyasa Yoga Teacher Training Program.

The attached document is an example of the certificate I received as a graduate from a teacher training program. You can use it as a template.

Stylistically, what you design can be: visually enticing, professional, clean, and modern.

Please develop the "Tidal Lotus" logo and embed it within the certificate.

Please add a circular watermark behind the body of the certificate similar to the one found in the attachment; leave out the words Asana Guild because I am not associated with that organization.

The name of my school is "Tidal Lotus." And it was established in 2017, which you can include.

The certificate affirms that "' 'such-and-such' has successfully completed the Tidal Lotus modern vinyasa yoga training, completing two hundred hours of instruction in practice and theory. Within the power of our institution as a certifying agent we declare Such-and-such, now, a teacher competent to share the gift of yoga with the masses in a safe and effective."

My name -Dennis Halvorsen- should be at bottom with a faux-signature; position title: Tidal Lotus founder.

If you decide to include text on the fringe, like the example, it might include bars of text describing the maxims of the Tidal Lotus school reading:

This is Tidal Lotus
Breath is primary
Evolve the physical culture
Bring your unique expression to the practice
Take Breaks
Freestyle
Close your eyes
Feel deeper into your body
This is active meditation
This is moving meditation
This is modern meditation

And find a way to integrate Emojis like: Fire, Water, Prayer Hands, etc. as you see fit.

Generally, make the certificate look: official, clear and clean. You can base it from the example given. And try and create a graphic design that is more visually capturing then the example.

```html
<!DOCTYPE html>
<html lang="en">
<head>
<meta charset="utf-8">
<title>Tidal Lotus Certificate of Completion</title>
<link rel="stylesheet" href="https://fonts.googleapis.com/css2?family=UnifrakturMaguntia&family=Open+Sans:wght@400;600;700&family=Merriweather:wght@700&display=swap">
<style>
  :root {
    --backdrop: #4d7189;
    --paper: #ffffff;
    --paper-warm: #fbf3e6;
    --crimson: #c21f2e;
    --crimson-dark: #8f1520;
    --navy: #142b57;
    --gold: #e2a52a;
    --gold-light: #f6dc6a;
    --ink: #1d1d1d;
    --rule: #444444;
    --mark: #cfcfd6;
  }
  * { margin: 0; padding: 0; box-sizing: border-box; }
  html, body { width: 880px; height: 1200px; overflow: hidden; }
  body { background: var(--backdrop); position: relative; font-family: "Open Sans", sans-serif; color: var(--ink); }

  .certificate {
    position: absolute; left: 132px; width: 616px; height: 474px;
    background: radial-gradient(circle at 56% 50%, var(--paper-warm) 0%, var(--paper) 60%);
    box-shadow: 0 10px 14px rgba(0,0,0,.45);
    overflow: hidden;
  }
  .certificate--plain { top: 78px; }
  .certificate--emoji { top: 556px; }

  .watermark { position: absolute; left: 130px; top: 65px; width: 384px; height: 384px; }

  .ribbon { position: absolute; left: 0; top: 0; width: 160px; height: 250px; }
  .seal { position: absolute; left: 6px; top: 46px; width: 136px; height: 136px; }

  .title {
    position: absolute; right: 18px; top: 14px;
    font-family: "UnifrakturMaguntia", serif; font-size: 54px; line-height: 1;
    color: var(--crimson);
  }
  .subtitle {
    position: absolute; right: 30px; top: 88px;
    font-size: 23px; font-weight: 400; letter-spacing: .2px;
  }
  .affirm {
    position: absolute; left: 180px; width: 310px; top: 167px; text-align: center;
    font-family: "Merriweather", serif; font-weight: 700; font-size: 13.5px;
  }
  .name-line { position: absolute; left: 192px; width: 308px; top: 247px; border-top: 1px solid var(--rule); }
  .statement {
    position: absolute; top: 268px; width: 520px; text-align: center;
    font-size: 14.2px; line-height: 20.3px;
  }
  .certificate--plain .statement { left: 86px; }
  .certificate--emoji .statement { left: 101px; }

  .sign { position: absolute; top: 416px; width: 102px; border-top: 1px solid var(--rule); }
  .sign--date { left: 102px; }
  .sign--founder { left: 304px; }
  .sign-label {
    position: absolute; top: 426px; text-align: center;
    font-size: 9px; font-weight: 700; line-height: 16px; text-transform: uppercase;
  }
  .sign-label--date { left: 102px; width: 102px; }
  .sign-label--founder { left: 284px; width: 142px; }

  .corner { position: absolute; right: 0; bottom: 0; width: 210px; height: 130px; }

  .emoji { position: absolute; left: 42px; width: 54px; height: 56px; border-radius: 50%; }
  .emoji--fire { top: 254px; background: radial-gradient(circle at 50% 65%, #ffd27a 0%, #f58a4a 55%, #e4533a 100%); border-radius: 50% 50% 46% 46% / 60% 60% 40% 40%; }
  .emoji--prayer { top: 334px; background: linear-gradient(180deg, #f7d8a8 0%, #f0c48b 60%, #8fa6d8 100%); border-radius: 40% 40% 12% 12%; }
  .emoji--water { top: 410px; left: 50px; width: 40px; background: radial-gradient(circle at 40% 60%, #d8f1ff 0%, #7fc8f4 55%, #3b9ae0 100%); border-radius: 50% 50% 50% 50% / 30% 30% 70% 70%; }
</style>
</head>
<body>

<section class="certificate certificate--plain">
  <svg class="watermark" viewBox="0 0 384 384" role="img" aria-label="Faint circular school watermark">
    <circle cx="192" cy="192" r="180" fill="none" stroke="var(--mark)" stroke-width="10" opacity=".7"/>
    <circle cx="192" cy="192" r="150" fill="var(--mark)" opacity=".12"/>
  </svg>
  <svg class="ribbon" viewBox="0 0 160 250">
    <polygon points="30,0 118,0 118,242 74,212 30,242" fill="var(--crimson)"/>
    <polygon points="30,160 118,160 118,242 74,212 30,242" fill="var(--crimson-dark)" opacity=".5"/>
    <line x1="39" y1="0" x2="39" y2="232" stroke="var(--gold)" stroke-width="1.5"/>
    <line x1="109" y1="0" x2="109" y2="232" stroke="var(--gold)" stroke-width="1.5"/>
  </svg>
  <svg class="seal" viewBox="0 0 136 136" role="img" aria-label="Award seal">
    <circle cx="68" cy="68" r="67" fill="var(--navy)"/>
    <circle cx="68" cy="68" r="52" fill="#dfe3ea"/>
    <circle cx="68" cy="68" r="30" fill="var(--gold)"/>
    <circle cx="68" cy="68" r="22" fill="var(--gold-light)"/>
  </svg>

  <h1 class="title">Certificate</h1>
  <p class="subtitle">OF COMPLETION</p>
  <p class="affirm">THE CERTIFICATE AFFIRMS THAT</p>
  <div class="name-line"></div>
  <p class="statement">has successfully completed the Tidal Lotus modern vinyasa yoga training,<br>completing two hundred hours of instruction in practice and theory.<br>Within the power of our institution as a certifying agent we declare you,<br>now a teacher competent to share the gift of yoga with the masses<br>in a safe and effective."</p>

  <div class="sign sign--date"></div>
  <div class="sign sign--founder"></div>
  <p class="sign-label sign-label--date">Date</p>
  <p class="sign-label sign-label--founder">Dennis Halvorsen<br>Yoga Founder</p>

  <svg class="corner" viewBox="0 0 210 130" preserveAspectRatio="none">
    <polygon points="210,0 210,130 0,130" fill="var(--crimson)"/>
    <polygon points="210,26 210,130 14,130" fill="var(--gold)"/>
    <polygon points="210,40 210,130 30,130" fill="var(--crimson-dark)"/>
    <polygon points="210,50 210,130 48,130" fill="var(--navy)"/>
  </svg>
</section>

<section class="certificate certificate--emoji">
  <svg class="watermark" viewBox="0 0 384 384" role="img" aria-label="Faint circular school watermark">
    <circle cx="192" cy="192" r="180" fill="none" stroke="var(--mark)" stroke-width="10" opacity=".7"/>
    <circle cx="192" cy="192" r="150" fill="var(--mark)" opacity=".12"/>
  </svg>
  <svg class="ribbon" viewBox="0 0 160 250">
    <polygon points="30,0 118,0 118,242 74,212 30,242" fill="var(--crimson)"/>
    <polygon points="30,160 118,160 118,242 74,212 30,242" fill="var(--crimson-dark)" opacity=".5"/>
    <line x1="39" y1="0" x2="39" y2="232" stroke="var(--gold)" stroke-width="1.5"/>
    <line x1="109" y1="0" x2="109" y2="232" stroke="var(--gold)" stroke-width="1.5"/>
  </svg>
  <svg class="seal" viewBox="0 0 136 136" role="img" aria-label="Award seal">
    <circle cx="68" cy="68" r="67" fill="var(--navy)"/>
    <circle cx="68" cy="68" r="52" fill="#dfe3ea"/>
    <circle cx="68" cy="68" r="30" fill="var(--gold)"/>
    <circle cx="68" cy="68" r="22" fill="var(--gold-light)"/>
  </svg>

  <div class="emoji emoji--fire" role="img" aria-label="Fire emoji"></div>
  <div class="emoji emoji--prayer" role="img" aria-label="Prayer hands emoji"></div>
  <div class="emoji emoji--water" role="img" aria-label="Water drop emoji"></div>

  <h1 class="title">Certificate</h1>
  <p class="subtitle">OF COMPLETION</p>
  <p class="affirm">THE CERTIFICATE AFFIRMS THAT</p>
  <div class="name-line"></div>
  <p class="statement">has successfully completed the Tidal Lotus modern vinyasa yoga training,<br>completing two hundred hours of instruction in practice and theory.<br>Within the power of our institution as a certifying agent we declare you,<br>now a teacher competent to share the gift of yoga with the masses<br>in a safe and effective."</p>

  <div class="sign sign--date"></div>
  <div class="sign sign--founder"></div>
  <p class="sign-label sign-label--date">Date</p>
  <p class="sign-label sign-label--founder">Dennis Halvorsen<br>Yoga Founder</p>

  <svg class="corner" viewBox="0 0 210 130" preserveAspectRatio="none">
    <polygon points="210,0 210,130 0,130" fill="var(--crimson)"/>
    <polygon points="210,26 210,130 14,130" fill="var(--gold)"/>
    <polygon points="210,40 210,130 30,130" fill="var(--crimson-dark)"/>
    <polygon points="210,50 210,130 48,130" fill="var(--navy)"/>
  </svg>
</section>

</body>
</html>
```